Business Card Design, including supply of raw art files plus a vector diagram of the zelvon logo and

We need the business card design for a company that is launching a new exciting product. The brief requires the submission of the following once the final design is chosen:

- business card layout including raw files
- a composite vector image file of the zelvon logo and tag line
- a standalone vector image file of the zelvon logo

The product will be launched as a customer engagement app.

It has 4 core modules which enables a person to do multiple things - book tours and activities, order takeaways, search for local deals and offers. A universal currency is at the heart of this product. When you use the app, you earn cashback rewards when shopping or buying at any of the merchant partners across the modules as . These rewards can then be used as full or part payment when buying goods or services at these merchant partners.

The business card must help us build the brand, communicate the benefit of the brand's key focus - the ability to earn and burn this universal cashback ccurrency - across the 4 modules - booking of tours and activities, ordering, searching for local deals and payment.

We would like the design to use the brand's blue colour the hex colour is: 00
Dark grey : 646464
Darker blue shadow: 058bdd
Main Blue: 0084ff

We need to translate this into a CMYK print or spot colour print.

Both print options to be supplied as separate files.

An example of the base concept we have in mind is attached for your reference.

The font used by the brand is Proxima Nova.

Note: the duration has been set as 2 days.

Industry/Entity Type

Business

Contact Information for Business Card

Carla Mendoza
Marketing
W: www.zelvon.example
M: + 61 400555123
T: +61 2 5550 1473
A: Suite 7, Level 2, 14-18 Harwick Street, Sydney, NSW, 2000, Australia

Font styles to use
Sans Serif

Requirements
Must have
• zelVon logo and tagline
• address details
• zelVon icons as supplied
Nice to have
• would like to have the option of a spot varnish layer over the logo and icons at the back of the card

```html
<!DOCTYPE html>
<html lang="en">
<head>
<meta charset="utf-8">
<title>zelVon Business Card</title>
<link href="https://fonts.googleapis.com/css2?family=Montserrat:wght@300;400&display=swap" rel="stylesheet">
<style>
  :root {
    --backdrop: #a9a9a9;
    --card-white: #ffffff;
    --brand-blue: #3a75b3;
    --mark-blue: #1a8fd6;
    --text-grey: #5a5a5a;
    --divider: #9a9a9a;
    --white: #ffffff;
  }
  * { margin: 0; padding: 0; box-sizing: border-box; }
  html, body { width: 1200px; height: 754px; overflow: hidden; }
  body {
    background: var(--backdrop);
    font-family: "Montserrat", sans-serif;
    font-weight: 300;
    position: relative;
  }
  .card {
    position: absolute;
    top: 219px;
    width: 548px;
    height: 315px;
    box-shadow: 0 6px 14px rgba(0,0,0,0.35);
  }
  .card-front { left: 46px; background: var(--card-white); }
  .card-back { left: 606px; background: var(--brand-blue); border: 1px solid #d4dbe4; }

  .front-mark {
    position: absolute; left: 158px; top: 47px;
    width: 68px; height: 68px; border-radius: 50%;
    background: var(--mark-blue);
  }
  .front-name {
    position: absolute; left: 239px; top: 52px;
    font-size: 48px; line-height: 1; color: var(--text-grey); font-weight: 300;
  }
  .front-url {
    position: absolute; left: 242px; top: 112px;
    font-size: 19px; color: var(--text-grey); letter-spacing: 0.3px;
  }
  .person {
    position: absolute; right: calc(548px - 262px); top: 203px;
    text-align: right; color: var(--text-grey);
  }
  .person-name { font-size: 17px; line-height: 1.2; }
  .person-role { font-size: 13px; line-height: 1.3; }
  .divider {
    position: absolute; left: 277px; top: 209px;
    width: 1px; height: 39px; background: var(--divider);
  }
  .contacts {
    position: absolute; left: 293px; top: 203px;
    font-size: 13px; line-height: 16px; color: var(--text-grey);
    list-style: none;
  }
  .address-band {
    position: absolute; left: 0; bottom: 0; width: 100%; height: 53px;
    background: var(--brand-blue);
    color: var(--white); font-size: 13.5px; text-align: center;
    padding-top: 9px;
  }

  .back-mark {
    position: absolute; left: 116px; top: 57px;
    width: 92px; height: 92px; border-radius: 50%;
    background: var(--white);
  }
  .back-name {
    position: absolute; left: 222px; top: 62px;
    font-size: 60px; line-height: 1; color: var(--white); font-weight: 300;
  }
  .tagline {
    position: absolute; right: calc(548px - 430px); top: 122px;
    font-size: 19px; color: var(--white);
  }
  .modules {
    position: absolute; left: 0; top: 222px; width: 100%;
    list-style: none;
  }
  .module {
    position: absolute; width: 90px; margin-left: -45px;
    text-align: center; color: var(--white);
  }
  .module svg { display: block; margin: 0 auto; width: 36px; height: 36px; }
  .module-label { display: block; font-size: 8px; margin-top: 9px; font-weight: 400; }
</style>
</head>
<body>
  <section class="card card-front">
    <div class="front-mark"></div>
    <div class="front-name">zelVon</div>
    <div class="front-url">www.zelvon.example</div>

    <div class="person">
      <div class="person-name">Carla Mendoza</div>
      <div class="person-role">Marketing</div>
    </div>
    <div class="divider"></div>
    <ul class="contacts">
      <li>M: + 61 400555123</li>
      <li>T&nbsp; : +61 2 5550 1473</li>
      <li>W: www.zelvon.example</li>
    </ul>

    <div class="address-band">Suite 7, Level 2, 14-18 Harwick Street, Sydney, NSW, 2000, Australia</div>
  </section>

  <section class="card card-back">
    <div class="back-mark"></div>
    <div class="back-name">zelVon</div>
    <div class="tagline">the cloud currency</div>

    <ul class="modules">
      <li class="module" style="left:146px">
        <svg viewBox="0 0 36 36" aria-hidden="true">
          <circle cx="18" cy="18" r="8" fill="#fff"/>
          <text x="18" y="22" text-anchor="middle" font-size="11" font-family="Montserrat, sans-serif" font-weight="400" fill="#3a75b3">$</text>
          <path d="M6 12 A13 13 0 0 1 22 5" stroke="#fff" stroke-width="3" fill="none"/>
          <path d="M20 1 L25 5 L19 9 Z" fill="#fff"/>
          <path d="M30 24 A13 13 0 0 1 14 31" stroke="#fff" stroke-width="3" fill="none"/>
          <path d="M16 27 L11 31 L17 35 Z" fill="#fff"/>
        </svg>
        <span class="module-label">CashBack Rewards</span>
      </li>
      <li class="module" style="left:236px">
        <svg viewBox="0 0 36 36" aria-hidden="true">
          <path d="M4 11 H11 L14 7 H22 L25 11 H32 V30 H4 Z" fill="#fff"/>
          <circle cx="18" cy="20" r="6.5" fill="#3a75b3"/>
          <circle cx="18" cy="20" r="4.5" fill="#fff"/>
        </svg>
        <span class="module-label">Tours &amp; Activities</span>
      </li>
      <li class="module" style="left:325px">
        <svg viewBox="0 0 36 36" aria-hidden="true">
          <line x1="8" y1="4" x2="28" y2="33" stroke="#fff" stroke-width="2.5"/>
          <path d="M6 3 V10 M9 3 V10 M12 3 V10" stroke="#fff" stroke-width="1.5"/>
          <line x1="29" y1="7" x2="8" y2="33" stroke="#fff" stroke-width="2.5"/>
          <ellipse cx="29" cy="6" rx="4" ry="5.5" transform="rotate(35 29 6)" fill="#fff"/>
        </svg>
        <span class="module-label">Mobile Ordering</span>
      </li>
      <li class="module" style="left:415px">
        <svg viewBox="0 0 36 36" aria-hidden="true">
          <path d="M20 3 H33 V16 L16 33 L3 20 Z" fill="#fff"/>
          <circle cx="27" cy="9" r="2.5" fill="#3a75b3"/>
        </svg>
        <span class="module-label">Local Offers</span>
      </li>
    </ul>
  </section>
</body>
</html>
```